Specialty Chemical Product Line Card Revamp

I need a new digital brochure for our product catalog of various chemicals. This will be sent to my customers as a digital file or printed on flat paper (not a folded brochure). I have included the OLD brochure (Tobin Chemical Line Card document) and the new categories that I want used instead (Line Card Categories document). I also included our logo and other photos. I would like the new brochure to be more modern and attention-grabbing

Target Market(s)

Product Manufacturers

Industry/Entity Type

Chemical Product

Font styles to use
Serif
Sans Serif

Requirements
Must have
• Product Category Headers. Company Logo
Nice to have
• Incorporate the attached photos. Use similar colors as the logo. Fit on 2 pages
Should not have
• Cannot be more than 3 pages.

```html
<!DOCTYPE html>
<html lang="en">
<head>
<meta charset="utf-8">
<title>Tobin Chemical — Product Catalog</title>
<link href="https://fonts.googleapis.com/css2?family=Lato:wght@400;700;900&family=Oswald:wght@500;600&display=swap" rel="stylesheet">
<style>
:root{
  --navy:#1b3a7c;
  --navy-deep:#122c63;
  --green:#6cab3b;
  --green-dark:#4f8f2a;
  --panel:#e3e5e7;
  --ink:#26282b;
  --paper:#ffffff;
  --stage:#5d5d5d;
  --photo-lab-a:#e9f1f7;
  --photo-lab-b:#9cc3de;
  --photo-site-a:#dfe5ea;
  --photo-site-b:#aeb8c2;
}
*{box-sizing:border-box;margin:0;padding:0}
html,body{width:902px;height:1200px;overflow:hidden}
body{background:var(--stage);font-family:"Lato",Arial,sans-serif;color:var(--ink);position:relative}
.page{position:absolute;background:var(--paper);overflow:hidden;box-shadow:0 6px 14px rgba(0,0,0,.45)}
.page-cover{left:92px;top:71px;width:328px;height:461px}
.page-inner{left:84px;top:622px;width:329px;height:465px;background:linear-gradient(#f1f2f3,#ffffff 60%)}
.page-back{left:524px;top:349px;width:328px;height:461px;background:linear-gradient(#f1f2f3,#ffffff 50%)}
.layer{position:absolute;left:0;top:0}
.brand{position:absolute;font-family:"Lato",Arial,sans-serif;font-weight:400;color:var(--navy);letter-spacing:.2px;white-space:nowrap}
.brand-cover{left:24px;top:28px;font-size:23px}
.brand-back{left:16px;top:272px;font-size:15px}
.catalog-title{position:absolute;left:30px;top:130px;color:#fff;font-family:"Oswald",Arial,sans-serif;font-weight:500;line-height:1.05;text-transform:uppercase}
.catalog-title .line-1{font-size:17px;display:block}
.catalog-title .line-2{font-size:13px;display:block}
.card{position:absolute;background:var(--panel);border-radius:6px;box-shadow:0 1px 2px rgba(0,0,0,.12);overflow:hidden}
.card-head{background:linear-gradient(var(--green),var(--green-dark));color:#fff;font-family:"Oswald",Arial,sans-serif;font-weight:600;font-size:8px;text-transform:uppercase;text-align:center;border-radius:6px 6px 0 0;height:17px;line-height:17px;letter-spacing:.3px}
.card-head.tall{height:24px;line-height:8px;padding-top:4px}
.card-head.tall-single{height:24px;line-height:24px}
.card-body{list-style:none;padding:5px 7px;font-size:4.3px;line-height:1.32;color:var(--ink)}
.cols-2{column-count:2;column-gap:6px}
.cols-3{column-count:3;column-gap:6px}
.cols-4{column-count:4;column-gap:6px}
.card-body li{break-inside:avoid}
.footer-contact{position:absolute;color:#fff;font-size:6.5px;font-weight:700;left:0;width:100%;text-align:center;line-height:1.6}
.footer-contact svg{vertical-align:-1px;margin-right:3px}
</style>
</head>
<body>

<section class="page page-cover">
  <svg class="layer" width="328" height="461" viewBox="0 0 328 461">
    <defs>
      <linearGradient id="lab" x1="0" y1="0" x2="1" y2="1">
        <stop offset="0" stop-color="var(--photo-lab-a)"/><stop offset="1" stop-color="var(--photo-lab-b)"/>
      </linearGradient>
      <linearGradient id="band" x1="0" y1="0" x2="1" y2="0">
        <stop offset="0" stop-color="#173a86"/><stop offset=".7" stop-color="#2e5a9e" stop-opacity=".85"/><stop offset="1" stop-color="#5f8fc0" stop-opacity=".3"/>
      </linearGradient>
    </defs>
    <rect x="0" y="0" width="328" height="225" fill="url(#lab)" role="img" aria-label="Photo of laboratory glassware with a pipette dropping blue liquid"/>
    <path d="M0 0H200C160 30 120 58 0 80Z" fill="#fff"/>
    <path d="M0 80C90 66 170 40 230 0H246C190 46 100 80 0 92Z" fill="var(--green)"/>
    <path d="M0 98C120 86 230 70 328 60V210H0Z" fill="url(#band)"/>
    <path d="M0 205C100 196 220 212 328 198V222C220 232 110 220 0 226Z" fill="var(--green)"/>
    <path d="M0 215C110 206 220 222 328 212V461H0Z" fill="#fff"/>
    <path d="M0 428C90 418 220 432 328 418V461H0Z" fill="var(--navy)"/>
    <path d="M0 424C100 414 220 428 328 413V418C220 432 90 418 0 428Z" fill="var(--green)"/>
  </svg>
  <div class="brand brand-cover">Tobin Chemical</div>
  <h1 class="catalog-title"><span class="line-1">Product Catalog</span><span class="line-2">of Various Chemicals</span></h1>

  <div class="card" style="left:12px;top:220px;width:138px;height:208px">
    <div class="card-head">Solvents</div>
    <ul class="card-body cols-2">
      <li>Acetate, N-butyl</li><li>Acetate, N-propyl</li><li>Acetone</li><li>Aliphatic Solvents</li><li>Amyl Acetate</li><li>Aromatic Solvents</li><li>Butyl Acetate</li><li>Cyclohexane</li><li>Cyclohexanone</li><li>DB Acetate</li><li>DE Acetate</li><li>Diisobutyl Ketone</li><li>Dimethylformamide</li><li>EB Acetate</li><li>Ethyl Acetate</li><li>Ethyl Ether, Reagent</li><li>Ethylene Dichloride</li><li>Heptane</li><li>Hexane</li><li>Isobutyl Acetate</li><li>Isophorone</li><li>Isopropyl Acetate</li><li>Kerosene</li><li>Methyl Amyl Ketone</li><li>Diethylene Glycol Methyl Ether</li><li>Glycol Methyl Ether</li><li>Methyl Ethyl Ketone</li><li>Methyl Isoamyl Ketone</li><li>Methyl Isobutyl Ketone</li><li>Methyl Salicylate</li><li>Methylene Chloride</li><li>Mineral Spirits</li><li>Mineral Spirits, Odorless</li><li>n-Butyl Pyrrolidone</li><li>n-Propyl Bromide</li><li>Perchloroethylene</li><li>Petroleum Ether</li><li>PM Acetate</li><li>Sodium Acetate</li><li>Solvent 100</li><li>Solvent 150</li><li>Tetrahydrofuran</li><li>Toluene</li><li>Trichloroethylene</li><li>Turpentine</li><li>Xylene</li>
    </ul>
  </div>
  <div class="card" style="left:155px;top:220px;width:78px;height:208px">
    <div class="card-head">Alcohols</div>
    <ul class="card-body">
      <li>Butanol</li><li>Cyclohexanol</li><li>Denatured Alcohol</li><li>Diacetone Alcohol</li><li>DBE</li><li>Diethylene Glycol</li><li>Dipropylene Glycol</li><li>Inhibited Propylene Glycol</li><li>Inhibited Ethylene Glycol</li><li>Ethyl Alcohol 190 Proof</li><li>Ethyl Alcohol 200 Proof</li><li>Ethylene Glycol</li><li>Glycerine</li><li>Glycol Ether Acetates</li><li>Hexylene Glycol</li><li>Isobutyl Alcohol</li><li>Isopropyl Alcohol</li><li>Methanol</li><li>Methyl Amyl Alcohol</li><li>n-Butyl Alcohol</li><li>n-Propyl Alcohol</li><li>Polyethylene Glycols</li><li>Propylene Glycol, Industrial</li><li>Propylene Glycol, USP</li><li>Secondary Butyl Alcohol</li><li>Sorbitol</li><li>Tripropylene Glycol</li><li>Triethylene Glycol</li>
    </ul>
  </div>
  <div class="card" style="left:238px;top:220px;width:78px;height:208px">
    <div class="card-head">Acids</div>
    <ul class="card-body">
      <li>Acetic Acid 28%, 56%, 75%, 80%</li><li>Acetic Acid Glacial 99.5%</li><li>Acetic Acid, Reagent</li><li>Boric Acid</li><li>Chromic Acid</li><li>Citric Acid, USP</li><li>Citric Acid, Liquid</li><li>EDTA Tetrasodium</li><li>Fluoboric Acid 48-50%</li><li>Formic Acid</li><li>Glacial Acetic Acid</li><li>Gluconic Acid</li><li>Glycolic Acid</li><li>Hydrochloric Acid</li><li>Hydrochloric Acid Reagent</li><li>Hydrofluoric Acid</li><li>Hydrofluosilicic Acid 25%</li><li>Lactic Acid</li><li>Muriatic Acid 18°, 20°, 22°</li><li>Muriatic Acid, Inhibited</li><li>Nitric Acid</li><li>Nitric Acid, Reagent</li><li>Oxalic Acid</li><li>Phosphoric Acid 75%, 85%, Tech</li><li>Phosphoric Acid, Reagent</li><li>Sorbic Acid</li><li>Sulfamic Acid</li><li>Sulfuric Acid 66°</li><li>Sulfuric Acid, Reagent</li>
    </ul>
  </div>

  <div class="footer-contact" style="top:436px">
    <div><svg width="6" height="6" viewBox="0 0 10 10"><circle cx="5" cy="5" r="5" fill="#fff"/><path d="M3 2.5l1.2 1-0.6 1a4 4 0 0 0 1.9 1.9l1-0.6 1 1.2-1 1C4.7 7.8 2.2 5.3 2 3.5Z" fill="var(--navy)"/></svg>555-014-2290</div>
    <div><svg width="6" height="6" viewBox="0 0 10 10"><circle cx="5" cy="5" r="4.2" fill="none" stroke="#fff" stroke-width="1.3"/><path d="M1 5h8M5 1c-2 2.5-2 5.5 0 8M5 1c2 2.5 2 5.5 0 8" stroke="#fff" stroke-width=".8" fill="none"/></svg>www.tobinchemco.com</div>
  </div>
</section>

<section class="page page-inner">
  <svg class="layer" width="329" height="465" viewBox="0 0 329 465">
    <defs>
      <linearGradient id="truck" x1="0" y1="0" x2="0" y2="1">
        <stop offset="0" stop-color="#b9cfe0"/><stop offset=".45" stop-color="#6f8fa6"/><stop offset=".7" stop-color="#2c3f6e"/><stop offset="1" stop-color="#5d6468"/>
      </linearGradient>
    </defs>
    <rect x="0" y="0" width="329" height="330" fill="#eceef0" role="img" aria-label="Faint photo of a warehouse interior with shelving"/>
    <rect x="0" y="330" width="329" height="135" fill="url(#truck)" role="img" aria-label="Photo of a blue delivery truck with a white trailer on a highway"/>
  </svg>

  <div class="card" style="left:17px;top:37px;width:71px;height:108px">
    <div class="card-head">Oils</div>
    <ul class="card-body">
      <li>Naphthenic Base Oil</li><li>D-Limonene</li><li>Kerosene</li><li>Mineral Seal Oil</li><li>Neatsfoot Oil</li><li>Naphtha, V.M. &amp; P.</li><li>Naphthenic Oils</li><li>Pine Oil</li><li>V.M. &amp; P. Naphtha</li><li>Vanishing Oil</li><li>Way Lubricants</li><li>White Kerosene</li><li>White Oils</li>
    </ul>
  </div>
  <div class="card" style="left:93px;top:37px;width:230px;height:108px">
    <div class="card-head">Solids</div>
    <ul class="card-body cols-3">
      <li>Activated Carbon</li><li>Anhydrous Ammonia</li><li>Aluminum Sulfate</li><li>Barium Carbonate</li><li>Bicarbonate of Soda</li><li>CCH Granular 65%</li><li>Calcium Borate</li><li>Calcium Chloride, flake or pellets</li><li>Calcium Nitrate</li><li>Caustic Potash, flake</li><li>Caustic Soda, beads or flake</li><li>Citric Acid, USP</li><li>Copper Cyanide</li><li>Copper Sulfate, crystal</li><li>Dipotassium Phosphate, FCC</li><li>Disodium Phosphate, FCC</li><li>Epsom Salts</li><li>Manganese Sulfate, dry</li><li>Muriate of Potash</li><li>Nickel Chloride, dry</li><li>Nickel Sulfate, salt</li><li>Clay Adsorbent</li><li>Potassium Carbonate</li><li>Rochelle Salts</li><li>Rock Salt</li><li>Sodium Bisulfate, Anhy. G.B.S.</li><li>Sodium Citrate, USP granular</li><li>Sodium Metasilicate, Anhy.</li><li>Sodium Sulfate, Anhydrous</li><li>Sodium Thiosulfate, dry</li><li>Sodium Tripolyphosphate, Gran.</li><li>Tetra Sodium Pyro Phosphate</li><li>Zinc Dust</li>
    </ul>
  </div>

  <div class="card" style="left:17px;top:155px;width:306px;height:110px">
    <div class="card-head">Metals &amp; Salts</div>
    <ul class="card-body cols-4">
      <li>Aluminum Chloride</li><li>Aluminum Sulfate</li><li>Bicarbonate of Soda</li><li>Borax 5 mol, pentahydrate</li><li>Cadmium Oxide</li><li>Calcium Acetate</li><li>Calcium Bromide</li><li>Calcium Chloride, liquid</li><li>Calcium Nitrate</li><li>Chlorine, gas, liquid or dry</li><li>Copper Anodes</li><li>Copper Cyanide</li><li>Copper Sulfate, Crystal</li><li>DDBSA</li><li>Dipotassium Phosphate, FCC</li><li>Ferric Chloride DWG</li><li>Ferric Sulfate</li><li>Ferrous Sulfate (Copperas)</li><li>Iron Phosphates</li><li>Lime, hydrated</li><li>Lithium Carbonate</li><li>Magnesium Chloride</li><li>Magnesium Hydroxide</li><li>Magnesium Oxide</li><li>Magnesium Sulfate</li><li>Manganese Carbonate</li><li>Manganese Sulfate, liquid or dry</li><li>Monoethanolamine Phosphate</li><li>Monopotassium Phosphate</li><li>Nickel Acetate</li><li>Nickel Anodes</li><li>Nickel Chloride, solution</li><li>Nickel Fluoborate</li><li>Nickel Sulfate, solution</li><li>Phosphates</li><li>Polyphosphates</li><li>Potassium Copper Cyanide</li><li>Potassium Alum</li><li>Potassium Carbonate</li><li>Potassium Chloride</li><li>Potassium Cyanide</li><li>Potassium Permanganate</li><li>Rochelle Salts</li><li>Rock Salt</li><li>Soda Ash</li><li>Soap</li><li>Stannous Fluoborate, solution</li><li>Stannous Sulfate</li><li>Sulfur</li><li>Sulfur Dioxide</li><li>Tetra Potassium Pyro Phosphate</li><li>Tetrahydrate</li><li>Tricalcium Phosphate</li><li>Copper Vitriol</li><li>Zinc Anodes</li><li>Zinc Chloride</li><li>Zinc Cyanide</li><li>Zinc Oxide</li>
    </ul>
  </div>

  <div class="card" style="left:17px;top:272px;width:71px;height:88px">
    <div class="card-head">Amines</div>
    <ul class="card-body">
      <li>Cyclohexylamine</li><li>DEA 99%</li><li>Diethylamine</li><li>Diethanolamine</li><li>Dimethyl Ethanolamine</li><li>Ethylenediamine</li><li>Monoethanolamine</li><li>Morpholine</li><li>Triethanolamine 85%, 99%</li><li>Triethylamine</li>
    </ul>
  </div>
  <div class="card" style="left:93px;top:272px;width:230px;height:113px">
    <div class="card-head">Sodium Compounds</div>
    <ul class="card-body cols-3">
      <li>Disodium Phosphate, FCC</li><li>Monosodium Phosphate</li><li>Sodium Acetate</li><li>Sodium Benzoate</li><li>Sodium Bichromate</li><li>Sodium Bisulfate, Anhy. G.B.S.</li><li>Sodium Bisulfite, liquid</li><li>Sodium Bicarbonate</li><li>Sodium Bifluoride</li><li>Sodium Carbonate</li><li>Sodium Chlorate</li><li>Sodium Citrate, USP granular</li><li>Sodium Fluoride</li><li>Sodium Gluconate</li><li>Sodium Hexametaphosphate, Tech</li><li>Sodium Hexametaphosphate, Food</li><li>Sodium Hydrosulfite</li><li>Sodium Hypochlorite</li><li>Sodium Metasilicate, Anhy.</li><li>Sodium Metasilicate, Pent.</li><li>Sodium Molybdate</li><li>Sodium Nitrate</li><li>Sodium Nitrite</li><li>Sodium Percarbonate</li><li>Sodium Permanganate</li><li>Sodium Persulfate</li><li>Sodium Acid Pyrophosphate</li><li>Sodium Silicate</li><li>Sodium Silicofluoride</li><li>Sodium Sulfate</li><li>Sodium Sulfide</li><li>Sodium Sulfite, Anhydrous</li><li>Sodium Thiosulfate, liquid or dry</li><li>Sodium Tripolyphosphate, Anhy.</li><li>Sodium Tripolyphosphate, Gran.</li><li>Tetra Sodium Pyro Phosphate, FCC</li><li>Trisodium Phosphate</li>
    </ul>
  </div>
</section>

<section class="page page-back">
  <svg class="layer" width="328" height="461" viewBox="0 0 328 461">
    <defs>
      <linearGradient id="site" x1="0" y1="0" x2="0" y2="1">
        <stop offset="0" stop-color="#ffffff"/><stop offset=".35" stop-color="var(--photo-site-a)"/><stop offset=".7" stop-color="var(--photo-site-b)"/><stop offset="1" stop-color="#8b9196"/>
      </linearGradient>
    </defs>
    <rect x="0" y="0" width="328" height="248" fill="#eceef0" role="img" aria-label="Faint photo of a warehouse interior with shelving"/>
    <rect x="0" y="248" width="328" height="180" fill="url(#site)" role="img" aria-label="Photo of the company's grey warehouse building with loading dock doors"/>
    <path d="M0 432C100 420 230 436 328 420V461H0Z" fill="var(--navy)"/>
    <path d="M0 428C100 416 230 432 328 415V420C230 436 100 420 0 432Z" fill="var(--green)"/>
  </svg>

  <div class="card" style="left:15px;top:15px;width:103px;height:98px">
    <div class="card-head tall">Ammonium<br>Compounds</div>
    <ul class="card-body">
      <li>Ammonium Bicarbonate</li><li>Ammonium Chloride, Treated or Untreated</li><li>Ammonium Bifluoride</li><li>Ammonium Hydroxide 21, 26</li><li>Ammonium Hydroxide, Reagent</li><li>Ammonium Nitrate</li><li>Ammonium Persulfate</li><li>Ammonium Sulfate</li><li>Anhydrous Ammonia</li><li>Monoammonium Phosphate</li>
    </ul>
  </div>
  <div class="card" style="left:125px;top:15px;width:193px;height:98px">
    <div class="card-head tall-single">Miscellaneous</div>
    <ul class="card-body cols-2">
      <li>All Purpose Cleaner</li><li>Bleach</li><li>Carbon Remover</li><li>Caustic Soda Liquid 50%, Diaphragm Grade</li><li>Caustic Soda Liquid, Membrane Grade</li><li>Distilled Water</li><li>Inhibited Propylene Glycol</li><li>Heat Transfer Glycol</li><li>Formaldehyde 37%</li><li>Hydrogen Peroxide, Tech, Food Grade</li><li>Potassium Silicate</li><li>Quick Dry Absorbent</li><li>Soaps</li><li>Polyols</li><li>Urea</li><li>Windshield Washer Solvent</li>
    </ul>
  </div>

  <div class="card" style="left:22px;top:127px;width:296px;height:116px">
    <div class="card-head">By Function</div>
    <ul class="card-body cols-4">
      <li>Antifoams</li><li>Antifreeze</li><li>Bucket / Roller Wash</li><li>Chelating Agents</li><li>Chlorinated Solvents</li><li>Cleaners, Floor, Metal, Soak, Steam</li><li>Coolants</li><li>Corrosion Inhibitors</li><li>Cutting Oils</li><li>Dechlorinators</li><li>Defoamers</li><li>Degreasing Solvents</li><li>De-Icers</li><li>Descaling Acid</li><li>Electro Cleaners</li><li>Filter Powders</li><li>Floor Absorbents</li><li>Foam Control</li><li>Form Oils</li><li>Gear Oils</li><li>Heat Transfer Fluids</li><li>Hydraulic Fluids</li><li>Inhibited Glycol Fluids</li><li>Lacquer Reducers</li><li>Lacquer Thinners</li><li>Laboratory Chemicals</li><li>Metal Conditioners</li><li>Metalworking Lubricants</li><li>Nonionic Surfactants</li><li>Paint Strippers</li><li>Paint Thinners</li><li>Process Oils</li><li>Reagent Acids</li><li>Reagent Solvents</li><li>Rubber Rejuvenator</li><li>Rust Proofers</li><li>Safety Absorbent</li><li>Safety Solvents</li><li>Soak Cleaners</li><li>Soluble Oils</li><li>Steam Cleaners</li><li>Surfactants</li><li>Synthetic Coolants</li><li>Thinners</li><li>Waste Water Treatment Solutions</li><li>Water Soluble Oils</li><li>Wetting Agents</li>
    </ul>
  </div>

  <div class="brand brand-back">Tobin Chemical</div>

  <div class="footer-contact" style="top:437px">
    <div><svg width="6" height="6" viewBox="0 0 10 10"><circle cx="5" cy="5" r="5" fill="#fff"/><path d="M3 2.5l1.2 1-0.6 1a4 4 0 0 0 1.9 1.9l1-0.6 1 1.2-1 1C4.7 7.8 2.2 5.3 2 3.5Z" fill="var(--navy)"/></svg>555-014-2290</div>
    <div><svg width="6" height="6" viewBox="0 0 10 10"><circle cx="5" cy="5" r="4.2" fill="none" stroke="#fff" stroke-width="1.3"/><path d="M1 5h8M5 1c-2 2.5-2 5.5 0 8M5 1c2 2.5 2 5.5 0 8" stroke="#fff" stroke-width=".8" fill="none"/></svg>www.tobinchemco.com</div>
  </div>
</section>

</body>
</html>
```